Business Card Design Project for Female Personal Trainer

I need a business card design to appeal to female clients for my personal training and group fitness boot camp business called 'Lumeva Studios'. It should be girly, fun and have an active/healthy pic or figure incorporated into the business name.

Target Market(s)

- Females 20-65yrs

Industry/Entity Type

Training

Font styles to use
Serif
Sans Serif

Colors
e34197
e567a6

Requirements
Must have
• First Side of Business Card Details :

Corin Delph
MASTER PERSONAL TRAINER
Cert III & Cert IV in Fitness
Senior First Aid
Mobile: 0438 507 164
Email: lumeva@quillpost.net
Facebook: Lumeva Studios

* Mobile Personal Training *Individual Sessions *Bootcamp *Weight-loss and Toning

Second Side of Business Card I want to offer a free personal consult:
Something like this:

Need direction with your health & fitness goals?

Call now for your free 1 on 1 Personal Training Session with full consultation

Nice to have
• Have a sub-heading for example:

'Promoting healthy living through fitness & nutrition'

- have the colour pink or blue (to appeal to a female)

- a picture/motif//logo attached (sometimes a picture paints a thousand words)

Should not have
• * picture of a person with big muscles or appeal to a man (I'm training women only)

* should not be busy or crammed up look (if I've added to much info above please just use to your discretion).

```html
<!DOCTYPE html>
<html lang="en">
<head>
<meta charset="utf-8">
<title>Lumeva Studios – Business Card</title>
<link rel="stylesheet" href="https://fonts.googleapis.com/css2?family=Ubuntu:wght@400;500;700&display=swap">
<style>
  :root {
    --pink: #e34197;
    --pink-soft: #e567a6;
    --blue: #1f8ccb;
    --blue-faint: #cfe6f4;
    --card: #fbfbfb;
    --backdrop: #2b2b2b;
  }
  * { box-sizing: border-box; margin: 0; padding: 0; }
  html, body { width: 1200px; height: 1023px; overflow: hidden; }
  body {
    background: var(--backdrop);
    font-family: "Ubuntu", sans-serif;
    display: flex;
    flex-direction: column;
    align-items: center;
    justify-content: center;
    gap: 30px;
  }
  .card {
    position: relative;
    width: 840px;
    height: 480px;
    background: var(--card);
    overflow: hidden;
    box-shadow: 0 6px 18px rgba(0,0,0,.45);
  }

  /* Front */
  .faint-ring {
    position: absolute;
    right: 40px;
    top: 20px;
    width: 360px;
    height: 360px;
    border-radius: 50%;
    border: 22px solid var(--blue-faint);
    opacity: .7;
    z-index: 0;
  }
  .brand {
    position: absolute;
    display: flex;
    align-items: center;
    gap: 12px;
    z-index: 1;
  }
  .brand-front { left: 50px; top: 240px; }
  .brand-name {
    font-weight: 700;
    color: var(--pink);
    font-size: 42px;
    letter-spacing: -1px;
    white-space: nowrap;
  }
  .brand-dot {
    width: 58px;
    height: 58px;
    border-radius: 50%;
    border: 6px solid var(--blue);
    flex: none;
  }
  .details {
    position: absolute;
    left: 490px;
    top: 56px;
    width: 310px;
    z-index: 1;
  }
  .person-name {
    font-size: 34px;
    font-weight: 500;
    color: var(--pink);
    margin-bottom: 6px;
  }
  .role { font-size: 17px; color: var(--blue); letter-spacing: .3px; }
  .cert { font-size: 16px; color: var(--pink); line-height: 1.35; }
  .contact { list-style: none; margin-top: 18px; }
  .contact li {
    display: flex;
    align-items: center;
    gap: 9px;
    font-size: 17px;
    color: var(--blue);
    margin-bottom: 8px;
  }
  .contact svg { width: 16px; height: 16px; flex: none; }
  .services {
    position: absolute;
    left: 0;
    right: 0;
    bottom: 34px;
    text-align: center;
    font-size: 19px;
    font-weight: 700;
    color: var(--pink);
    z-index: 1;
  }

  /* Back */
  .brand-back {
    left: 50%;
    top: 150px;
    transform: translateX(-50%);
  }
  .offer {
    position: absolute;
    right: 50px;
    bottom: 40px;
    text-align: right;
    color: var(--pink);
    font-weight: 700;
    font-size: 19px;
    line-height: 1.9;
  }
</style>
</head>
<body>

  <section class="card card-front">
    <div class="faint-ring" aria-hidden="true"></div>

    <div class="brand brand-front">
      <span class="brand-name">Lumeva Studios</span>
      <span class="brand-dot" aria-hidden="true"></span>
    </div>

    <div class="details">
      <h1 class="person-name">Corin Delph</h1>
      <p class="role">MASTER PERSONAL TRAINER</p>
      <p class="cert">Cert III &amp; Cert IV in Fitness</p>
      <p class="cert">Senior First Aid</p>
      <ul class="contact">
        <li>
          <svg viewBox="0 0 16 16" aria-hidden="true"><rect x="4" y="1" width="8" height="14" rx="1.5" fill="none" stroke="var(--pink)" stroke-width="1.6"/><circle cx="8" cy="12.3" r=".9" fill="var(--pink)"/></svg>
          0438 507 164
        </li>
        <li>
          <svg viewBox="0 0 16 16" aria-hidden="true"><rect x="1" y="1" width="14" height="14" rx="2" fill="var(--pink)"/></svg>
          Lumeva Studios
        </li>
        <li>
          <svg viewBox="0 0 16 16" aria-hidden="true"><rect x="1" y="3" width="14" height="10" rx="1.5" fill="var(--pink)"/><path d="M1.5 4l6.5 5 6.5-5" fill="none" stroke="#fff" stroke-width="1.3"/></svg>
          lumeva@quillpost.net
        </li>
      </ul>
    </div>

    <p class="services">Mobile Personal Training *Individual Sessions *Bootcamp *Weight-loss and Toning</p>
  </section>

  <section class="card card-back">
    <div class="brand brand-back">
      <span class="brand-name">Lumeva Studios</span>
      <span class="brand-dot" aria-hidden="true"></span>
    </div>

    <div class="offer">
      <p>Need direction with your health &amp; fitness goals?</p>
      <p>Call now for your free 1 on 1 Personal Training Session with full consultation</p>
    </div>
  </section>

</body>
</html>
```